Life Insurance Landing Page (for lead gen)

We need a high converting life insurance page created. It will be housed at www.CoverageVerifyHub.com. We will be driving former life insurance prospects to this page where they will only need to confirm their phone number & email in order to receive an updated quote.
Updates

Only the page design is required, the coding will be done on our end. 

Target Market(s)

People who have expressed an interest in obtaining life insurance.

Industry/Entity Type

Life Insurance

Requirements
Must have
• 1) Under "CoverageVerifyHub.com" Please include a "Powered by KRBT" tag and match the colors of this site: http://thekrbt.com/life-insurance-services.html to the page.

2) The form should ask for their phone number and include an appointment calendar widget (we'll code the functionality) so they can choose the date/time of their call. It should also have an email confirmation field.

3) the overall message next to the form fields should be "Thanks for visiting Gordon (we'll personalize this "firstname" field ), please let us know the best time to schedule a brief call so we can give you an updated, rock bottom pricing quote on a policy. We'll also email you with the information, please confirm your email here and we'll send you the details.

4) We'd like to include a box that appears to be a personalized "quote briefing" snapshot that will list this information: "Name: _________" "Birth Date:"____________" "Policy Type: _______", "Coverage Amount: ____________" " all these fields will be populated into the page.

```html
<!DOCTYPE html>
<html lang="en">
<head>
<meta charset="utf-8">
<title>CoverageVerifyHub.com – Life Insurance Quote</title>
<link href="https://fonts.googleapis.com/css2?family=Roboto:wght@400;500;700&family=Roboto+Condensed:wght@700&display=swap" rel="stylesheet">
<style>
:root{
  --blue:#1d7fc0;
  --blue-dark:#15659e;
  --teal:#2aa7c4;
  --green:#7cc242;
  --text:#3a3a3a;
  --muted:#6b6b6b;
  --line:#d9dfe3;
  --field:#eef2f5;
  --white:#ffffff;
}
*{box-sizing:border-box;margin:0;padding:0}
html,body{width:667px;height:1200px;overflow:hidden}
body{
  position:relative;font-family:"Roboto",Arial,sans-serif;color:var(--text);
  background:
    radial-gradient(ellipse 260px 420px at 20px 950px,#8cc63f 0%,rgba(140,198,63,0) 70%),
    radial-gradient(ellipse 300px 500px at 40px 400px,#3fb7d1 0%,rgba(63,183,209,0) 75%),
    radial-gradient(ellipse 280px 500px at 660px 780px,#39a8d8 0%,rgba(57,168,216,0) 75%),
    radial-gradient(ellipse 260px 300px at 20px 60px,#d6e48a 0%,rgba(214,228,138,0) 75%),
    linear-gradient(180deg,#d5eef0 0%,#b8e3ec 40%,#9fd6e6 70%,#d3ecef 100%);
}
.page{position:absolute;left:105px;width:457px}

/* header */
.site-header{top:0;height:36px;background:linear-gradient(90deg,#7cc242 0%,#3ea99b 40%,#1d86b8 70%,#1d7fc0 100%);border-bottom:2px solid var(--white)}
.brand{position:absolute;left:17px;top:3px;color:var(--white)}
.brand-name{font-size:16px;font-weight:700;line-height:17px}
.brand-tag{font-size:8px;font-weight:700}

/* hero */
.hero{top:50px;height:241px;background:linear-gradient(180deg,#e4f4f9 0%,#c9e8f2 100%);overflow:hidden}
.hero-photo{position:absolute;right:0;top:0;width:240px;height:241px;background:radial-gradient(ellipse at 60% 55%,#f0d2bd 0%,#b8d3e3 55%,#9cc8de 100%)}
.hero-copy{position:absolute;left:19px;top:22px;width:236px;z-index:1}
.hero-title{font-size:19.5px;font-weight:500;color:var(--blue);line-height:23px;white-space:nowrap}
.hero-lead{font-size:8.3px;line-height:10px;margin-top:2px;color:#333}
.field{position:absolute;left:19px;width:171px;height:18px;background:var(--field);border:1px solid #cdd6dc;font-size:7.5px;color:#8a9aa4;padding:4px 5px}
.field b{color:var(--blue);font-weight:400}
.schedule{position:absolute;left:19px;top:177px;font-size:8px;color:#444}
.schedule .lbl{position:absolute;top:5px}
.mini-field{position:absolute;top:0;height:18px;background:var(--field);border:1px solid #cdd6dc;font-size:6.8px;color:#8a9aa4;padding:4px 4px;white-space:nowrap}
.btn{display:block;background:linear-gradient(180deg,#2a93d6,#176aa6);color:var(--white);font-size:8px;text-align:center;border-radius:2px;border-bottom:2px solid #0f4f7e}
.hero-submit{position:absolute;left:19px;top:198px;width:40px;height:18px;padding-top:4px}

/* calendar */
.calendar{position:absolute;left:143px;top:238px;width:181px;height:117px;background:rgba(255,255,255,.94);box-shadow:0 1px 4px rgba(0,0,0,.25);z-index:5;font-size:6.5px}
.cal-head{display:flex;justify-content:space-between;padding:5px 6px 2px;font-size:7.5px;color:#333}
.cal-head i{color:#999;font-style:italic}
.cal-grid{display:grid;grid-template-columns:repeat(7,1fr);text-align:center;row-gap:3px;padding:0 4px}
.cal-grid .dow{color:#888;font-size:5.5px}
.cal-grid .off{color:#c8c8c8}
.cal-grid .today{color:var(--blue)}
.cal-grid .sel{background:var(--blue);color:var(--white)}
.cal-foot{display:flex;justify-content:center;gap:22px;margin-top:5px;font-size:5.5px;font-weight:700}
.cal-foot .clear{color:#c0392b}

/* intro section */
.panel{background:var(--white);border-bottom:3px solid var(--blue)}
.intro{top:313px;height:146px}
.intro-title{position:absolute;left:18px;top:18px;font-size:16px;font-weight:400;color:var(--blue)}
.intro-photo{position:absolute;left:19px;top:42px;width:74px;height:80px;background:linear-gradient(180deg,#f4e38a 0%,#c6d85a 55%,#6fa33a 100%)}
.intro-text{position:absolute;left:102px;top:44px;width:228px;font-size:6.3px;line-height:9px;color:var(--muted)}
.intro-text h3{font-size:6.5px;font-weight:500;color:#333;margin-bottom:5px}
.intro-text p{margin-bottom:8px}
.offer{position:absolute;left:340px;top:22px;border-left:1px solid var(--line);padding-left:14px;height:100px;margin-left:-14px}
.offer h2{font-size:11.5px;font-weight:400;color:var(--blue);margin-bottom:6px}
.offer li{list-style:none;font-size:6.4px;line-height:12.8px;color:#333}
.offer li::before,.bullets li::before{content:"";display:inline-block;width:3px;height:3px;border-radius:50%;background:var(--blue);margin-right:4px;vertical-align:1px}

/* main */
.main{top:469px;height:690px}
.article{position:absolute;left:18px;top:20px;width:285px;font-size:6.2px;line-height:8.8px;color:var(--muted)}
.article h2{font-size:11px;font-weight:400;color:var(--blue);margin:0 0 5px}
.article p{margin-bottom:7px}
.article .sect{border-top:1px solid var(--line);padding-top:9px;margin-top:7px}
.bullets{margin-bottom:6px}
.bullets li{list-style:none;font-size:6.5px;line-height:12.6px;color:#333}
.divider{position:absolute;left:320px;top:20px;width:1px;height:655px;background:var(--line)}
.side{position:absolute;left:342px;width:100px;border:1px solid var(--line)}
.side-title{background:var(--blue);color:var(--white);font-family:"Roboto Condensed","Arial Narrow",sans-serif;font-weight:700;font-size:13px;text-align:center;padding:4px 0;white-space:nowrap;overflow:hidden}
.quote{top:23px;height:180px}
.quote-form{padding:6px 6px}
.quote-form label{display:block;font-size:6.3px;color:#555;margin-top:4px}
.quote-form .in{height:14px;border:1px solid #c9d1d6;margin-top:3px;background:var(--white)}
.side .btn{width:56px;height:15px;margin:10px auto 0;padding-top:3px}
.cta{top:219px;height:206px;background:linear-gradient(180deg,#bfe3f1 0%,#e9f5fb 45%,#ffffff 100%)}
.cta-title{font-family:"Roboto Condensed","Arial Narrow",sans-serif;font-weight:700;font-size:16px;color:var(--blue);text-align:center;padding-top:7px;white-space:nowrap}
.cta-text{font-size:8px;line-height:10px;text-align:center;color:#333;padding:3px 6px}
.cta-photo{position:absolute;left:6px;top:75px;width:88px;height:105px;background:radial-gradient(ellipse at 50% 40%,#d9b9a0 0%,#c9d9e4 60%,#eef5f9 100%)}
.cta-bar{position:absolute;left:0;bottom:0;width:100%;height:21px;background:var(--blue);color:var(--white);font-family:"Roboto Condensed","Arial Narrow",sans-serif;font-weight:700;font-size:11px;text-align:center;padding-top:4px;white-space:nowrap}
.news{top:437px;height:97px}
.news .side-title{font-size:10.5px;padding:5px 0}
.news-lbl{font-size:6.5px;color:#555;text-align:center;margin-top:8px}
.news .in{height:14px;border:1px solid #c9d1d6;margin:5px 6px 0}

/* footer */
.site-footer{position:absolute;left:105px;top:1170px;width:457px;text-align:center;font-size:5.6px;line-height:7px;color:#222}
</style>
</head>
<body>

<header class="page site-header">
  <div class="brand">
    <div class="brand-name">CoverageVerifyHub.com</div>
    <div class="brand-tag">Powered by KRBT</div>
  </div>
</header>

<section class="page hero">
  <div class="hero-photo" role="img" aria-label="Photo of a smiling family of three embracing"></div>
  <div class="hero-copy">
    <h1 class="hero-title">Thanks for visiting Gordon</h1>
    <p class="hero-lead">Please let us know the best time to schedule a brief call so we can give you an updated, rock bottom pricing quote on a policy. We'll also email you with the information, please confirm your email here and we'll send you the details.</p>
  </div>
  <div class="field" style="top:104px">Name<b>*</b></div>
  <div class="field" style="top:129px">Email<b>*</b></div>
  <div class="field" style="top:153px">Phone<b>*</b></div>
  <div class="schedule">
    <span class="lbl" style="left:0">Date</span>
    <svg style="position:absolute;left:21px;top:3px" width="12" height="12" viewBox="0 0 12 12"><rect x="1" y="2" width="10" height="9" fill="#fff" stroke="#1d7fc0"/><rect x="1" y="2" width="10" height="3" fill="#1d7fc0"/></svg>
    <div class="mini-field" style="left:39px;width:45px">05/04/2014</div>
    <span class="lbl" style="left:100px">Time</span>
    <svg style="position:absolute;left:120px;top:3px" width="12" height="12" viewBox="0 0 12 12"><circle cx="6" cy="6" r="5" fill="#fff" stroke="#1d7fc0" stroke-width="1.3"/><path d="M6 3v3h2.5" stroke="#1d7fc0" fill="none"/></svg>
    <div class="mini-field" style="left:137px;width:40px">10.25 AM</div>
  </div>
  <span class="btn hero-submit">Submit</span>
</section>

<div class="calendar">
  <div class="cal-head"><span>◀</span><span>April <i>2014</i></span><span>▶</span></div>
  <div class="cal-grid">
    <span class="dow">Sun</span><span class="dow">Mon</span><span class="dow">Tue</span><span class="dow">Wed</span><span class="dow">Thu</span><span class="dow">Fri</span><span class="dow">Sat</span>
    <span class="off">31</span><span>1</span><span>2</span><span>3</span><span class="today">4</span><span class="sel">5</span><span>6</span>
    <span>7</span><span>8</span><span>9</span><span>10</span><span>11</span><span>12</span><span>13</span>
    <span>14</span><span>15</span><span>16</span><span>17</span><span>18</span><span>19</span><span>20</span>
    <span>21</span><span>22</span><span>23</span><span>24</span><span>25</span><span>26</span><span>27</span>
    <span>28</span><span>29</span><span>30</span><span class="off">1</span><span class="off">2</span><span class="off">3</span><span class="off">4</span>
    <span class="off">5</span><span class="off">6</span><span class="off">7</span><span class="off">8</span><span class="off">9</span><span class="off">10</span><span class="off">11</span>
  </div>
  <div class="cal-foot"><span>Today</span><span class="clear">✕ Clear</span></div>
</div>

<section class="page panel intro">
  <h2 class="intro-title">Life Insurance</h2>
  <div class="intro-photo" role="img" aria-label="Photo of a family jumping in a sunny field"></div>
  <div class="intro-text">
    <h3>Fairlow California - What You Need To Know About Life Insurance</h3>
    <p>Having the right life insurance is pivotal in planning for the future of you and your loved ones. Life insurance can help you fulfill promises you've made your family when you are gone.</p>
    <p>Don't leave the future of you and your loved ones to chance. Keystone Ridge Benefit Trust can help you find the right life insurance coverage for you, and help ensure that your policy continually meets your needs.</p>
  </div>
  <div class="offer">
    <h2>What We Offer</h2>
    <ul>
      <li>Auto Insurance</li><li>Home Insurance</li><li>Life Insurance</li><li>Health Insurance</li><li>Business Insurance</li><li>Restaurant Insurance</li><li>Workers Comp</li>
    </ul>
  </div>
</section>

<main class="page panel main">
  <article class="article">
    <h2>Life changes - so should your policy</h2>
    <p>For each of our neighbors in California, the right life insurance will be unique for you and dependent on your personal and financial needs. As your life changes, your life insurance coverage may need to change in order to adapt to your current needs. Some life transformations that may require a policy "tune-up" and our help at Keystone Ridge Benefit Trust include:</p>
    <ul class="bullets">
      <li>You recently married or divorced</li>
      <li>You have a new child or grandchild</li>
      <li>You have opened or expanded a business</li>
      <li>Your health or your spouse's health has deteriorated</li>
      <li>You are providing care or financial assistance to a parent</li>
      <li>Your child or grandchild requires assistance or long-term care</li>
      <li>You recently purchased a new home</li>
      <li>You are planning for a child or grandchild's education</li>
      <li>You are concerned about retirement income</li>
      <li>You have refinanced your home mortgage in the past six months</li>
      <li>You or your spouse recently received an inheritance</li>
      <li>You have a sizable estate</li>
    </ul>
    <div class="sect">
      <h2>California - what you need to know about life insurance</h2>
      <p>KRBT can help you select the best life insurance coverage for your needs. There are several different types of life insurance products available – the most common include:</p>
    </div>
    <div class="sect">
      <h2>Term Life Insurance</h2>
      <p>Term life insurance provides protection for a specified period of time. If you do not currently have life insurance, term can be a good place to start. It's generally less expensive than permanent (whole) life insurance, and is available in varying time periods with fixed premiums from a one year (annual renewable term) to 20-year (level term) period. Furthermore, term life insurance is sometimes convertible to permanent coverage, providing you with flexibility as your needs change.</p>
    </div>
    <div class="sect">
      <h2>Whole Life Insurance</h2>
      <p>Whole life insurance is a form of permanent life insurance that remains in force for your entire lifetime, provided premiums are paid as specified in the policy. Whole life insurance can be an investment opportunity, as many whole life insurance policies also build cash value over time.</p>
    </div>
    <div class="sect">
      <h2>Universal Life Insurance</h2>
      <p>Universal life is a form of permanent life insurance characterized by its flexible premiums, face amounts and unbundled pricing structure. Universal life can build cash value, which earns an interest rate that may adjust periodically, but is usually guaranteed not to fall below a certain percentage.</p>
      <p>So what type of life insurance is best for you? Talk with the team at KRBT today at: 800-555-0147(KRBT), and we can assist in identifying the best protection for you.</p>
    </div>
    <div class="sect">
      <h2>What are the advantages of life insurance?</h2>
      <p>Having the right life insurance is essential to planning for your present, and your future. Not only can life insurance provide assurance for your family after you are gone, many life insurance options offer other benefits and investment opportunities you can take advantage of while you are living.</p>
      <p>Advantages of the life insurance death benefit: When you pass away, your life insurance provides income tax-free money to your named beneficiary or beneficiaries that can be used to pay funeral expenses, debt, tuition, estate taxes or virtually any financial need. Your policy can help provide security for your business as well, by enabling partners to buy out the interests of a deceased partner and prevent a forced liquidation.</p>
      <p>Advantages of Living Benefits: The cash value growth of a permanent (whole) life insurance policy is tax-deferred, meaning you do not pay taxes on the growth of cash value, unless money is withdrawn. Loans or withdrawals can be taken against the cash value of a permanent life insurance policy to help with expenses, such as college tuition or the down payment on a home.</p>
      <p>The right life insurance coverage for each and every one of our neighbors in California is unique – Call KRBT today to find out how to protect your family and your future with the right life insurance.</p>
    </div>
  </article>
  <div class="divider"></div>

  <aside class="side quote">
    <div class="side-title">Get A Free Quote</div>
    <div class="quote-form">
      <label>Name:</label><div class="in"></div>
      <label>Birth Date:</label><div class="in"></div>
      <label>Policy Type:</label><div class="in"></div>
      <label>Coverage Amount:</label><div class="in"></div>
      <span class="btn">Submit</span>
    </div>
  </aside>

  <aside class="side cta">
    <div class="cta-title">Need A Quote?</div>
    <p class="cta-text">Our Agents are ready to find out your needs and get you started</p>
    <div class="cta-photo" role="img" aria-label="Photo of a support agent wearing a headset"></div>
    <div class="cta-bar">Get Started Now</div>
  </aside>

  <aside class="side news">
    <div class="side-title">Signup For Newsletter</div>
    <p class="news-lbl">Enter email address</p>
    <div class="in"></div>
    <span class="btn">Submit</span>
  </aside>
</main>

<footer class="site-footer">
  Keystone Ridge Benefit Trust<br>
  48 W. Maple Ave. Fairlow, CA 90000 Phone (555) 014-2210 Fax (555) 014-2211<br>
  License #0934418
</footer>

</body>
</html>
```